We are a local Communty Pharmacy wishing to promote and market a specialised Pharmaceutical Service

We would like a design that is professional and enticing ( according to the brief In attached files)
We wish to Market Compounding Pharmacy as a specialist side of our business.
We have the expertise a purpose built preparation laboratory.
The main purpose is an Internet presence that entices prospective patients to contact or visit our physical store.

Target Market(s)

Patients Medicos and Veterinary clients

Industry/Entity Type

Pharmacy

Coding

Coded - Design and coding required

Number of Pages Required

1 page

Requirements
Must have
• Clear friendly image
Nice to have
• soft enticing feel
Should not have
• No crass loud unprofessional elements

```html
<!DOCTYPE html>
<html lang="en">
<head>
<meta charset="utf-8">
<title>Westbrook Compounding Pharmacy</title>
<link href="https://fonts.googleapis.com/css2?family=Open+Sans:wght@400;600;700;800&display=swap" rel="stylesheet">
<style>
:root{
  --green:#78b031;
  --blue:#1f8fd0;
  --text:#6a6a6a;
  --dark:#2d2d2d;
  --darker:#1f1f1f;
  --yellow:#f6b71c;
  --line:#e3e3e3;
  --white:#ffffff;
}
*{margin:0;padding:0;box-sizing:border-box}
html,body{width:1200px;height:2404px;overflow:hidden}
body{position:relative;font-family:"Open Sans",Arial,sans-serif;color:var(--text);background:var(--white)}
.site-header{height:150px;display:flex;align-items:center;padding:0 95px;border-bottom:1px solid var(--line)}
.brand{display:flex;align-items:center;gap:10px;width:330px}
.brand-mark{width:26px;height:26px;background:var(--blue);border-radius:50%}
.brand-name{font-weight:700;font-size:15px;color:var(--blue);line-height:1.15;width:150px}
.header-info{display:flex;gap:22px;font-size:10.5px;line-height:1.55}
.info-item{display:flex;gap:8px;align-items:flex-start}
.info-item svg{flex:none;margin-top:2px}
.info-item.address{width:220px}
.hero{position:relative;height:590px;background:linear-gradient(100deg,#e9e5df 0%,#f3f1ed 40%,#d9d2c8 75%,#b9ad9d 100%)}
.hero-photo{position:absolute;inset:0}
.hero-text{position:absolute;left:95px;top:345px}
.hero-title{font-weight:800;font-size:36px;color:var(--green);letter-spacing:.5px}
.hero-sub{font-weight:700;font-size:15px;color:#333;margin-top:14px;line-height:1.9}
.hero-arrow{position:absolute;top:280px;width:34px;height:34px;display:flex;align-items:center;justify-content:center}
.hero-arrow.prev{left:30px}.hero-arrow.next{right:30px}
.intro{padding:70px 95px 0}
.intro-title{font-weight:800;font-size:33px;color:var(--blue)}
.intro-title span{color:var(--green)}
.intro-body{margin-top:26px;font-size:11px;line-height:1.8}
.intro-body p{margin-bottom:27px}
.featured{padding-top:70px}
.featured-title{text-align:center;font-weight:700;font-size:22px;color:#333}
.featured-rule{width:1010px;margin:18px auto 0;border-top:1px solid var(--line)}
.cards{display:flex;gap:30px;padding:30px 95px 0}
.card{width:317px}
.card-head{background:var(--blue);color:var(--white);font-weight:700;font-size:15px;padding:8px 14px}
.card-image{height:160px}
.card-text{font-size:10.5px;line-height:1.6;padding:16px 0 14px}
.read-more{display:inline-block;background:var(--yellow);color:#333;font-weight:700;font-size:11px;padding:7px 14px}
.site-footer{position:absolute;top:2040px;left:0;width:1200px;height:315px;background:var(--dark);color:#bdbdbd;display:flex;padding:40px 95px 0;gap:60px}
.footer-col h3{color:var(--white);font-weight:700;font-size:18px;margin-bottom:24px}
.footer-col.hours{width:250px}
.footer-col.map{width:370px}
.footer-col.contacts{width:300px}
.hours-row{display:flex;gap:10px;font-size:11px;margin-bottom:10px}
.map-area{width:340px;height:190px;background:linear-gradient(135deg,#e8e6df,#d6dccd)}
.contact-row{display:flex;gap:12px;font-size:11px;line-height:1.55;margin-bottom:16px}
.contact-row svg{flex:none;margin-top:2px}
.bottom-bar{position:absolute;top:2355px;left:0;width:1200px;height:49px;background:var(--darker);display:flex;align-items:center;justify-content:space-between;padding:0 95px;font-size:10.5px;color:#9a9a9a}
.social{display:flex;gap:8px}
.social span{width:22px;height:22px;border:1px solid #777;border-radius:50%}
</style>
</head>
<body>
<header class="site-header">
  <div class="brand"><span class="brand-mark"></span><span class="brand-name">Westbrook Compounding Pharmacy</span></div>
  <div class="header-info">
    <div class="info-item address">
      <svg width="12" height="14" viewBox="0 0 12 14"><path d="M6 0a5 5 0 0 0-5 5c0 4 5 9 5 9s5-5 5-9a5 5 0 0 0-5-5zm0 7a2 2 0 1 1 0-4 2 2 0 0 1 0 4z" fill="#1f8fd0"/></svg>
      <div>Westbrook Community Pharmacy<br>Unit 3, Westbrook Plaza, 14 Harlow Road<br>Westbrook WA 6062</div>
    </div>
    <div>
      <div class="info-item"><svg width="12" height="12" viewBox="0 0 12 12"><path d="M2 0l2 3-1 1.5c.8 1.6 2 2.8 3.5 3.5L8 7l3 2-1.5 2.5C5 11 1 7 .5 2.5z" fill="#1f8fd0"/></svg><span>Phone (08) 9271 4500</span></div>
      <div class="info-item"><svg width="12" height="12" viewBox="0 0 12 12"><path d="M1 2h10v8H1z" fill="none" stroke="#1f8fd0"/></svg><span>Fax (08) 9271 4501</span></div>
      <div class="info-item"><svg width="12" height="12" viewBox="0 0 12 12"><path d="M1 2h10v8H1zM1 2l5 4 5-4" fill="none" stroke="#1f8fd0"/></svg><span>E: compounding@westbrookpharmacy.example</span></div>
    </div>
  </div>
</header>

<section class="hero">
  <div class="hero-photo" role="img" aria-label="White mortar and pestle on a pale wooden table"></div>
  <div class="hero-arrow prev"><svg width="18" height="30" viewBox="0 0 18 30"><path d="M15 2L3 15l12 13" fill="none" stroke="#fff" stroke-width="3"/></svg></div>
  <div class="hero-arrow next"><svg width="18" height="30" viewBox="0 0 18 30"><path d="M3 2l12 13L3 28" fill="none" stroke="#fff" stroke-width="3"/></svg></div>
  <div class="hero-text">
    <div class="hero-title">COMPOUNDING PHARMACY</div>
    <div class="hero-sub">IS<br>CUSTOMISED MEDICATIONS FOR PATIENTS</div>
  </div>
</section>

<section class="intro">
  <h1 class="intro-title"><span>WHAT IS</span> COMPOUNDING PHARMACY?</h1>
  <div class="intro-body">
    <p>Well ready for making these. The practice of making up medicines has been passed down from the 19th century and was formally superseded by the arrival of commercial drug manufacturing in the 1950s and 1960s.</p>
    <p>That led the greater extent of removing some of the physical workload from the pharmacist, freeing up the ability to counsel patients on their health and medication issues.</p>
    <p>We are not dismissing the evidence and use of commercial manufactured pharmaceuticals, and we certainly support their use and important position and in our society. Just there are many instances where 'one size does not fit all' and that is where we come in.</p>
    <p>Compounding pharmacy as a tool has recently moved to new technologies and techniques, enabling pharmacists the unique ability to compound medicines to specific needs.</p>
    <p>A pharmacist working with practitioners helps provide the framework for individually tailored prescription orders, addressing a documented medical condition for a specific patient.</p>
    <p>As a dedicated professional in our field we are constantly improving our strategic knowledge and skills, updating equipment in support of effective and consistent practice.</p>
    <p>We have set up a designated area with specialised equipment and are trained in the latest procedures with a view to ensure medicines are prepared to the highest standards.</p>
    <p>We also source our raw chemicals from only fully accredited suppliers adhering to strict pharmaceutical grade standards.</p>
    <p>Westbrook Community Pharmacy is accredited under the Regional Pharmacists Council as a Certified Care Pharmacy, as a means of industry quality assurance to ensure the highest quality of service is provided to our clients.</p>
    <p>Our ultimate goal as a compounding pharmacy is working with pharmaceutical needs aligned with the supportive ability of offering COMPOUNDED MEDICATIONS to assist the doctor and patient achieve a more positive therapeutic outcome.</p>
  </div>
</section>

<section class="featured">
  <h2 class="featured-title">FEATURED ITEMS</h2>
  <div class="featured-rule"></div>
  <div class="cards">
    <article class="card">
      <div class="card-head">Vet Article</div>
      <div class="card-image" role="img" aria-label="Veterinarian examining a dog" style="background:linear-gradient(135deg,#c9b39a,#7d8f9c)"></div>
      <p class="card-text">Tailored medicines for pets and working animals, made in flavours and strengths that suit each species and make dosing at home simple and stress free.</p>
      <span class="read-more">Read More</span>
    </article>
    <article class="card">
      <div class="card-head">Scar Therapy</div>
      <div class="card-image" role="img" aria-label="Hand applying cream to skin" style="background:linear-gradient(135deg,#e6cdb8,#b89680)"></div>
      <p class="card-text">Custom topical gels and creams that help soften and flatten scars, prepared to your prescriber's directions for sensitive or healing skin.</p>
      <span class="read-more">Read More</span>
    </article>
    <article class="card">
      <div class="card-head">Thyroid Extract</div>
      <div class="card-image" role="img" aria-label="Older woman speaking with a doctor" style="background:linear-gradient(135deg,#dcd6cf,#a9b3bd)"></div>
      <p class="card-text">Carefully measured thyroid preparations in precise doses, compounded for patients who need an alternative to standard commercial products.</p>
      <span class="read-more">Read More</span>
    </article>
  </div>
</section>

<footer class="site-footer">
  <div class="footer-col hours">
    <h3>OPENING HOURS</h3>
    <div class="hours-row"><span>Mon - Fri</span><span>8:30 am to 7:00 pm</span></div>
    <div class="hours-row"><span>Sat - Sun</span><span>9:00 am to 5:00 pm</span></div>
  </div>
  <div class="footer-col map">
    <h3>LOCATION MAP</h3>
    <div class="map-area" role="img" aria-label="Street map showing the pharmacy location"></div>
  </div>
  <div class="footer-col contacts">
    <h3>CONTACTS</h3>
    <div class="contact-row"><svg width="12" height="14" viewBox="0 0 12 14"><path d="M6 0a5 5 0 0 0-5 5c0 4 5 9 5 9s5-5 5-9a5 5 0 0 0-5-5zm0 7a2 2 0 1 1 0-4 2 2 0 0 1 0 4z" fill="#bdbdbd"/></svg><span>Westbrook Community Pharmacy<br>Unit 3, Westbrook Plaza, 14 Harlow Road<br>Westbrook WA 6062</span></div>
    <div class="contact-row"><svg width="12" height="12" viewBox="0 0 12 12"><path d="M2 0l2 3-1 1.5c.8 1.6 2 2.8 3.5 3.5L8 7l3 2-1.5 2.5C5 11 1 7 .5 2.5z" fill="#bdbdbd"/></svg><span>(08) 9271 4500</span></div>
    <div class="contact-row"><svg width="12" height="12" viewBox="0 0 12 12"><path d="M1 2h10v8H1z" fill="none" stroke="#bdbdbd"/></svg><span>(08) 9271 4501</span></div>
    <div class="contact-row"><svg width="12" height="12" viewBox="0 0 12 12"><path d="M1 2h10v8H1zM1 2l5 4 5-4" fill="none" stroke="#bdbdbd"/></svg><span>compounding@westbrookpharmacy.example</span></div>
  </div>
</footer>
<div class="bottom-bar">
  <span>© 2015 Westbrook Compounding Pharmacy. All Rights Reserved.</span>
  <div class="social"><span></span><span></span><span></span></div>
</div>
</body>
</html>
```